Automotive lighting company needs professional business card

Hello, we are an automotive lighting company and looking to have a professional business card designed for us. We have included some images which can be used on the card. Website is www.brightlanemotorparts.example which has all of our details on it. Email is brightlanemotorparts@mailbox.example phone number is 1300 862 317 thank you guys!

Target Market(s)

Automotive industry

Contact Information for Business Card

Phone - 1300 862 317
Web - www.brightlanemotorparts.example
Email - brightlanemotorparts@mailbox.example

Requirements
Must have
• Looking to have a dark theme. Elegant and professional. Needs to look and feel like a high quality card to represent high quality company.

```html
<!DOCTYPE html>
<html lang="en">
<head>
<meta charset="utf-8">
<title>Bright Lane Motor Parts – Business Card</title>
<link rel="stylesheet" href="https://fonts.googleapis.com/css2?family=Saira:wght@500;600;700&display=swap">
<style>
  :root {
    --backdrop: #56595e;
    --card-centre: #2b2d30;
    --card-edge: #0c0c0d;
    --brand-blue: #1b8fd2;
    --text-white: #f4f6f8;
    --rule: #8a8d92;
  }
  * { margin: 0; padding: 0; box-sizing: border-box; }
  html, body { width: 1125px; height: 1200px; overflow: hidden; }
  body {
    background: var(--backdrop);
    font-family: "Saira", "Arial Narrow", sans-serif;
    position: relative;
  }
  .card {
    position: absolute;
    left: 172px;
    width: 824px;
    height: 470px;
    background: radial-gradient(ellipse 60% 55% at 50% 45%, var(--card-centre), var(--card-edge));
    display: flex;
    flex-direction: column;
    align-items: center;
    justify-content: center;
    color: var(--text-white);
  }
  .card--front { top: 106px; }
  .card--back { top: 640px; }

  .holder-name {
    color: var(--brand-blue);
    font-weight: 600;
    font-size: 29px;
    letter-spacing: 0.5px;
    line-height: 1;
    margin-top: 20px;
  }
  .holder-role {
    display: flex;
    align-items: center;
    gap: 10px;
    width: 482px;
    margin-top: 6px;
    font-weight: 600;
    font-size: 18px;
    line-height: 1;
  }
  .holder-role::before, .holder-role::after {
    content: "";
    flex: 1;
    height: 1px;
    background: var(--rule);
  }
  .contact-line {
    font-weight: 500;
    font-size: 17px;
    margin-top: 18px;
    line-height: 1.5;
    text-align: center;
  }
  .contact-line .phone { font-weight: 600; font-size: 19px; }
  .contact-web { font-weight: 600; font-size: 17px; line-height: 1.4; }

  .brand-lockup {
    display: flex;
    align-items: center;
    gap: 14px;
    margin-top: 20px;
  }
  .brand-dot {
    width: 18px;
    height: 18px;
    border-radius: 50%;
    background: var(--brand-blue);
  }
  .brand-name {
    color: var(--brand-blue);
    font-weight: 700;
    font-size: 36px;
    letter-spacing: 1px;
    line-height: 1;
  }
  .brand-rule {
    width: 406px;
    height: 1px;
    background: var(--rule);
    margin-top: 12px;
  }
</style>
</head>
<body>
  <section class="card card--front">
    <h1 class="holder-name">DANIEL HARPER</h1>
    <p class="holder-role">PRESIDENT</p>
    <p class="contact-line"><span class="phone">1300 862 317</span> | brightlanemotorparts@mailbox.example</p>
    <p class="contact-web">www.brightlanemotorparts.example</p>
  </section>

  <section class="card card--back">
    <div class="brand-lockup">
      <span class="brand-dot"></span>
      <span class="brand-name">BRIGHT LANE MOTOR PARTS</span>
    </div>
    <div class="brand-rule"></div>
  </section>
</body>
</html>
```